Corporate Word-document templates

We need these documents templates for the following types of documentation:

- Proposal
- Report (meetings)
- Solution description (technical)
- Documentation

The front page of the documents can take inspiration from our PowerPoint template, website (https://www.lindqor.com/) and brand book. It should reflect our new branding guidelines.

See attached documents for structure and what we need them to contain. We need:
- front page
- generalt tekst page after the front page
- table of contents
- logo in upper right corner, page number + info in the footer, structure of tables
- anything else?

1) Make a design suggestion for the front page of the proposal and the Documentation
2) When we agree on the structure and front page, make the other two documents
3) we need all four documents with four different logos. 4 x 4 documents. the logos are: Marvelund, MVL, MVL Horizon & MVL Lens.

Target Market(s)

Large and medium corporations. Roles such as CEO, CFO, CIO, CTO, Controllers, Analysts, leaders/managers

Industry/Entity Type

Information Technology

Font styles to use
Sans Serif

Requirements
Must have
• - elements that are key to a word template
- four different word template files - each with the four different logos
- chose colors from our brand book

```html
<!DOCTYPE html>
<html lang="no">
<head>
<meta charset="utf-8">
<title>Marvelund dokumentmal – Administrasjon Vantage</title>
<link rel="stylesheet" href="https://fonts.googleapis.com/css2?family=Exo+2:wght@400;500;600;700;800&family=Mulish:wght@400;600;700;800&display=swap">
<style>
  :root{
    --stage:#c8c8c8;
    --navy:#0e2a4d;
    --navy-deep:#0a2240;
    --ocean:#1b6f95;
    --teal:#2a8fb4;
    --orange:#f29a1f;
    --ink:#1d1d1f;
    --body:#333;
    --heading:#2a5a9c;
    --paper:#ffffff;
    --footer:#222326;
    --label:#4a4a4a;
    --bezel:#141518;
    --screen-top:#3a4e60;
    --screen-bottom:#5c7385;
  }
  *{box-sizing:border-box;margin:0;padding:0}
  html,body{width:1200px;height:568px;overflow:hidden;background:var(--stage)}
  body{position:relative;font-family:"Mulish",sans-serif;color:var(--body)}

  .sheet{position:absolute;top:30px;width:342px;height:485px;background:var(--paper);overflow:hidden;box-shadow:0 1px 3px rgba(0,0,0,.25)}
  .sheet--cover{left:31px;width:340px}
  .sheet--toc{left:431px}
  .sheet--text{left:827px;width:343px}

  .sheet-label{position:absolute;top:528px;width:342px;text-align:center;font-family:"Exo 2",sans-serif;font-size:23px;font-weight:500;color:var(--label);letter-spacing:.5px}

  /* cover */
  .cover-hero{position:absolute;left:0;top:0;width:100%;height:316px;background:linear-gradient(160deg,var(--navy-deep) 0%,#123f66 40%,var(--ocean) 75%,var(--teal) 100%)}
  .cover-device{position:absolute;left:160px;top:120px;width:190px;height:226px;border-radius:14px 0 0 0;background:var(--bezel);padding:12px 0 0 12px}
  .cover-screen{width:100%;height:100%;background:linear-gradient(180deg,var(--screen-top),var(--screen-bottom))}
  .cover-title{position:absolute;left:54px;top:234px;font-family:"Exo 2",sans-serif;font-weight:500;font-size:22px;line-height:29px;color:#fff;text-shadow:0 1px 3px rgba(0,0,0,.35)}
  .cover-lower{position:absolute;left:0;top:316px;width:100%;height:159px;background:linear-gradient(90deg,#e4e6e8,#f4f5f6 60%,#fafafa)}
  .cover-curve{position:absolute;left:0;top:290px}
  .cover-meta{position:absolute;right:214px;top:372px;text-align:right;font-family:"Exo 2",sans-serif;font-size:10px;line-height:18.5px;color:var(--ink)}
  .cover-meta span{color:var(--navy)}
  .cover-rule{position:absolute;left:139px;top:370px;width:1px;height:76px;background:#7a8ea3}
  .cover-brand{position:absolute;left:166px;top:393px;display:flex;align-items:center;gap:7px;font-family:"Exo 2",sans-serif;font-weight:800;font-size:25px;color:var(--ink);letter-spacing:-.4px}
  .cover-brand i{display:block;width:10px;height:10px;background:var(--ink)}
  .cover-foot{position:absolute;left:0;bottom:0;width:100%;height:10px;background:var(--footer)}

  /* running header / footer */
  .page-head{position:absolute;left:0;top:0;width:100%;height:32px}
  .page-head svg{position:absolute;left:0;top:0}
  .page-title{position:absolute;left:10px;top:7px;font-family:"Exo 2",sans-serif;font-weight:500;font-size:14.5px;color:#fff}
  .page-brand{position:absolute;right:8px;top:11px;font-family:"Exo 2",sans-serif;font-weight:800;font-size:15px;color:var(--ink);letter-spacing:-.3px}
  .page-foot{position:absolute;left:0;bottom:0;width:100%;height:18px}
  .page-foot svg{position:absolute;left:0;top:0}
  .page-foot-text{position:absolute;left:6px;top:5px;font-family:"Exo 2",sans-serif;font-size:7px;color:#fff}
  .page-foot-brand{position:absolute;right:6px;top:4px;font-family:"Exo 2",sans-serif;font-weight:800;font-size:9px;color:var(--ink)}

  /* table of contents */
  .toc{position:absolute;left:21px;top:99px;width:299px;font-size:6.9px;color:var(--ink)}
  .toc-row{display:flex;align-items:baseline;height:12.8px}
  .toc-row--chapter{font-weight:700;margin-top:6px}
  .toc-row--first{margin-top:0}
  .toc-num{width:24px;flex:none}
  .toc-lead{flex:1;border-bottom:1px dotted #555;margin:0 2px;transform:translateY(-2px)}
  .toc-page{width:8px;text-align:right;flex:none}
  .toc-row--chapter .toc-page{width:12px}

  /* body text page */
  .content{position:absolute;left:19px;top:58px;width:300px}
  .content h1{font-size:9.5px;font-weight:700;color:var(--heading);margin-bottom:17px}
  .content h2{font-size:8.8px;font-weight:700;color:var(--heading);margin:10px 0 4px}
  .content p{font-size:6.3px;line-height:12.7px;color:var(--body)}
  .context-menu{margin:6px 0 8px;width:78px;font-size:5.6px;color:var(--ink)}
  .context-menu li{list-style:none;padding:2px 0 2px 7px;line-height:6px}
  .context-menu .is-active{background:#e8edf1;color:#2a5a6a}
  .filter-sample{margin-top:6px;width:136px;height:22px;background:linear-gradient(180deg,#f4f4f4 0 30%,#f5f08a 30% 48%,#eeeeee 48% 100%);border:1px solid #ddd}
</style>
</head>
<body>

<!-- Cover -->
<section class="sheet sheet--cover" aria-label="Forside">
  <div class="cover-hero"></div>
  <div class="cover-device" role="img" aria-label="Nettbrett som viser et dashbord med nøkkeltall og søylediagram"><div class="cover-screen"></div></div>
  <div class="cover-lower"></div>
  <svg class="cover-curve" width="340" height="40" viewBox="0 0 340 40" aria-hidden="true">
    <path d="M0 26 L305 26 C320 26 330 18 340 6 L340 40 L0 40 Z" fill="#e6e8ea"/>
    <path d="M0 26 L305 26 C320 26 330 18 340 6" fill="none" stroke="#ffffff" stroke-width="1.5" opacity=".8"/>
  </svg>
  <h1 class="cover-title">Administrasjon<br>Vantage<br>input-løsning</h1>
  <div class="cover-meta">
    Kunde: <span>Nordvik Fiber AS</span><br>
    Forfatter: <span>Eirik Solberg</span><br>
    Dato: <span>01.08.2019</span><br>
    Versjon: <span>1.0</span>
  </div>
  <div class="cover-rule"></div>
  <div class="cover-brand"><i></i>Marvelund</div>
  <div class="cover-foot"></div>
</section>
<div class="sheet-label" style="left:30px">COVER PAGE</div>

<!-- Table of contents -->
<section class="sheet sheet--toc" aria-label="Innholdsfortegnelse">
  <header class="page-head">
    <svg width="342" height="32" viewBox="0 0 342 32" aria-hidden="true">
      <rect width="342" height="32" fill="var(--navy)"/>
      <path d="M238 32 C262 12 295 4 342 3 L342 32 Z" fill="var(--orange)"/>
      <path d="M248 32 C270 15 300 7 342 6 L342 32 Z" fill="#fff"/>
    </svg>
    <div class="page-title">Project Heading Here</div>
    <div class="page-brand">Marvelund</div>
  </header>

  <nav class="toc">
    <div class="toc-row toc-row--first" style="font-weight:700"><span class="toc-label">Innhold</span><span class="toc-lead"></span><span class="toc-page">3</span></div>
    <div class="toc-row toc-row--chapter" style="margin-top:1px"><span class="toc-num">1</span><span class="toc-label">Generelt</span><span class="toc-lead"></span><span class="toc-page">4</span></div>
    <div class="toc-row"><span class="toc-num">1.1</span><span class="toc-label">Endre, lagre, angre</span><span class="toc-lead"></span><span class="toc-page">4</span></div>
    <div class="toc-row"><span class="toc-num">1.2</span><span class="toc-label">Ny rad</span><span class="toc-lead"></span><span class="toc-page">4</span></div>
    <div class="toc-row"><span class="toc-num">1.3</span><span class="toc-label">Slett rad</span><span class="toc-lead"></span><span class="toc-page">4</span></div>
    <div class="toc-row"><span class="toc-num">1.4</span><span class="toc-label">Filterrad</span><span class="toc-lead"></span><span class="toc-page">4</span></div>
    <div class="toc-row toc-row--chapter" style="margin-top:14px"><span class="toc-num">2</span><span class="toc-label">Administrasjon</span><span class="toc-lead"></span><span class="toc-page">5</span></div>
    <div class="toc-row"><span class="toc-num">2.1</span><span class="toc-label">Grunndata</span><span class="toc-lead"></span><span class="toc-page">5</span></div>
    <div class="toc-row"><span class="toc-num"></span><span class="toc-label">2.1.1 Partner</span><span class="toc-lead"></span><span class="toc-page">6</span></div>
    <div class="toc-row"><span class="toc-num"></span><span class="toc-label">2.1.2 Segment</span><span class="toc-lead"></span><span class="toc-page">6</span></div>
    <div class="toc-row"><span class="toc-num">2.2</span><span class="toc-label">Oppsett Måltall</span><span class="toc-lead"></span><span class="toc-page">6</span></div>
    <div class="toc-row"><span class="toc-num">2.3</span><span class="toc-label">Versjoner (Måltall)</span><span class="toc-lead"></span><span class="toc-page">7</span></div>
    <div class="toc-row"><span class="toc-num"></span><span class="toc-label">2.3.1 Gjenåpne en lukket versjon</span><span class="toc-lead"></span><span class="toc-page">8</span></div>
    <div class="toc-row"><span class="toc-num"></span><span class="toc-label">2.3.2 Sentralstyrte måltall</span><span class="toc-lead"></span><span class="toc-page">9</span></div>
    <div class="toc-row toc-row--chapter" style="margin-top:7px"><span class="toc-num">3</span><span class="toc-label">Varekost TV kanaler</span><span class="toc-lead"></span><span class="toc-page">9</span></div>
    <div class="toc-row toc-row--chapter" style="margin-top:7px"><span class="toc-num">4</span><span class="toc-label">Produktmapping</span><span class="toc-lead"></span><span class="toc-page">10</span></div>
    <div class="toc-row toc-row--chapter" style="margin-top:7px"><span class="toc-num">5</span><span class="toc-label">Teknisk</span><span class="toc-lead"></span><span class="toc-page">10</span></div>
    <div class="toc-row"><span class="toc-num">5.1</span><span class="toc-label">Installasjonsinformasjon</span><span class="toc-lead"></span><span class="toc-page">10</span></div>
    <div class="toc-row"><span class="toc-num">5.2</span><span class="toc-label">Automatisk jobb</span><span class="toc-lead"></span><span class="toc-page">11</span></div>
  </nav>

  <footer class="page-foot">
    <svg width="342" height="18" viewBox="0 0 342 18" aria-hidden="true">
      <rect width="342" height="18" fill="var(--footer)"/>
      <path d="M276 0 C290 0 292 18 304 18 L342 18 L342 0 Z" fill="#fff"/>
    </svg>
    <div class="page-foot-text">Side 4 av 11 &nbsp;|&nbsp; Administrasjon Vantage inputløsning for Nordvik Fiber AS</div>
    <div class="page-foot-brand">MVL Lens</div>
  </footer>
</section>
<div class="sheet-label" style="left:431px">PAGE - 01</div>

<!-- General text page -->
<section class="sheet sheet--text" aria-label="Generelt">
  <header class="page-head">
    <svg width="343" height="32" viewBox="0 0 343 32" aria-hidden="true">
      <rect width="343" height="32" fill="var(--navy)"/>
      <path d="M239 32 C263 12 296 4 343 3 L343 32 Z" fill="var(--orange)"/>
      <path d="M249 32 C271 15 301 7 343 6 L343 32 Z" fill="#fff"/>
    </svg>
    <div class="page-title">Project Heading Here</div>
    <div class="page-brand">Marvelund</div>
  </header>

  <article class="content">
    <h1>1 Generelt</h1>
    <h2 style="margin-top:0">1.1 Endre, lagre, angre</h2>
    <p>Felt som kan endres har en hvit bakgrunnsfarge.<br>
    Alle bilder har en «Lagre» og en «Hent» knapp.<br>
    Ulagrede endringer bekreftes ved å trykke på «Lagre»-knappen.<br>
    Ulagrede endringer angres i sin helhet ved å trykke på «Hent»-knappen, evt benyttes Ctrl-Z for å angre en og en endring.</p>

    <h2>1.2 Ny rad</h2>
    <p>Nye rader legges til ved å høyre-klikke i aktuelt skjema og velge en av følgende:</p>
    <ul class="context-menu">
      <li>Sett inn rad</li>
      <li class="is-active">Sett inn rad under</li>
      <li>Sett inn kopi av rad</li>
    </ul>
    <p>Velges sett inn kopi av rad, settes det inn en ny rad lik raden som var aktiv i det høyre-klikk ble gjort.<br>
    Merk at en ny rad er å betrakte som en ulagret endring og må derfor enten bekreftes ved å trykke «Lagre» eller angres å trykke «Hent»</p>

    <h2>1.3 Slett rad</h2>
    <p>Eksisterende rader slettes ved å høyre-klikke i aktuelt skjema og velge:<br>
    Merk at en slettet rad er å betrakte som en ulagret endring og må derfor enten bekreftes ved å trykke «Lagre» eller angres å trykke «Hent»<br>
    Ikke alle skjermbilder gir mulighet for sletting av rader.</p>

    <h2>1.4 &nbsp;Filterrad</h2>
    <p>Enkelte skjermbilder har en filterrad mellom overskriftsrad og data, for eksempel:</p>
    <div class="filter-sample" role="img" aria-label="Skjermutklipp av tabell med gul filterrad under overskriftene"></div>
  </article>

  <footer class="page-foot">
    <svg width="343" height="18" viewBox="0 0 343 18" aria-hidden="true">
      <rect width="343" height="18" fill="var(--footer)"/>
      <path d="M277 0 C291 0 293 18 305 18 L343 18 L343 0 Z" fill="#fff"/>
    </svg>
    <div class="page-foot-text">Side 4 av 11 &nbsp;|&nbsp; Administrasjon Vantage inputløsning for Nordvik Fiber AS</div>
    <div class="page-foot-brand">MVL Lens</div>
  </footer>
</section>
<div class="sheet-label" style="left:827px">PAGE - 02</div>

</body>
</html>
```